SOS! The Thistle cafe is in need of a menu face lift!

We need a standout looking menu for our evolving cafe. Our business has grown greatly from our fresh and changing menu, however the menu (look) itself isn't inspiring and is basic.
I have attached some photos of the business and menus I like the look of.
I am open to other ideas (this is why I need your creative help)
Our menu is currently on an A5 clip board, however we are willing to change it a different size if needed.

Would love to have it a multi function eg, used as a takeaway menu as well, possibly bi-fold? Added Wednesday, June 8, 2016

• It would be cool to have some old sea/ pirate references?

```html
<!DOCTYPE html>
<html lang="en">
<head>
<meta charset="utf-8">
<title>The Thistle Menu</title>
<link href="https://fonts.googleapis.com/css2?family=Bree+Serif&family=Roboto+Slab:wght@300;400;700&display=swap" rel="stylesheet">
<style>
:root{
  --backdrop:#d9d9d9;
  --board:#2a2a2a;
  --board-dark:#1f1f1f;
  --chalk:#f1efe9;
  --chalk-soft:#bdbab3;
  --red:#a51e2d;
}
*{box-sizing:border-box;margin:0;padding:0}
html,body{width:1200px;height:1200px;overflow:hidden;background:var(--backdrop)}
body{display:flex;align-items:center;justify-content:center;font-family:"Roboto Slab",serif;color:var(--chalk)}
.menu-sheet{
  position:relative;width:830px;height:1160px;
  background:radial-gradient(ellipse at 40% 35%,#333 0%,var(--board) 55%,var(--board-dark) 100%);
  padding:36px 34px 30px 40px;
  display:grid;grid-template-columns:372px 1fr;grid-template-rows:1fr auto;
}
.col-breakfast{position:relative;padding-left:46px;padding-right:22px;display:flex;flex-direction:column}
.col-lunch{position:relative;border-left:2px dashed var(--chalk);padding-left:26px;display:flex;flex-direction:column}
.brand{display:flex;align-items:center;justify-content:center;gap:12px;margin:30px 0 46px;font-family:"Bree Serif",serif;font-size:34px;line-height:1;color:var(--chalk)}
.brand-dot{width:14px;height:14px;border-radius:50%;background:var(--chalk)}
.side-rule{position:absolute;left:18px;top:150px;bottom:150px;width:2px;background:var(--red)}
.side-title{
  position:absolute;left:-4px;top:470px;transform:rotate(-90deg);transform-origin:left top;
  font-weight:700;color:var(--red);font-size:26px;letter-spacing:1px;white-space:nowrap;
}
.side-title small{font-size:13px;margin-left:10px;letter-spacing:1px}
.item{margin-bottom:9px}
.item-row{display:flex;align-items:baseline;gap:6px}
.item-name{font-family:"Bree Serif",serif;font-size:15.5px;white-space:nowrap}
.item-row .leader{flex:1;border-bottom:1px solid var(--chalk-soft);transform:translateY(-3px);min-width:14px}
.item-price{font-family:"Bree Serif",serif;font-size:13.5px;white-space:nowrap}
.item-desc{font-size:9.5px;line-height:1.35;color:var(--chalk-soft);font-weight:300}
.item-row .item-desc{white-space:nowrap}
.item-desc b{font-weight:700;color:var(--chalk)}
.extras{position:relative;margin-top:auto;padding-top:8px}
.extras-row{display:flex;gap:12px;align-items:baseline;margin-bottom:6px}
.extras-row .price{font-family:"Bree Serif",serif;font-size:15px;width:40px}
.extras-row .list{font-size:9.5px;color:var(--chalk-soft)}
.extras-label{position:absolute;left:-44px;bottom:-4px;transform:rotate(-90deg);transform-origin:left top;font-size:11px;color:var(--red);letter-spacing:1px;text-transform:uppercase;white-space:nowrap}
.footer{grid-column:1 / 3;border-top:2px solid var(--red);margin:14px 0 0 18px;padding-top:8px;text-align:center;font-size:10.5px;line-height:1.5}
.lunch-band{display:flex;align-items:center;gap:10px;background:var(--red);margin:48px -8px 22px -26px;padding:10px 16px;color:var(--chalk)}
.lunch-band h1{font-weight:700;font-size:30px;line-height:0.95;text-transform:uppercase;text-align:center}
.lunch-band .hours{border-left:1px solid var(--chalk);padding-left:10px;font-family:"Bree Serif",serif;font-size:12.5px;line-height:1.35}
.section-head{text-align:center;margin:10px 0 4px}
.section-head span{display:inline-block;border:1.5px solid var(--red);padding:2px 16px;font-size:10px;letter-spacing:2px;text-transform:uppercase}
.section-note{text-align:center;font-size:9.5px;color:var(--chalk-soft);margin-bottom:10px;font-weight:300}
</style>
</head>
<body>
<main class="menu-sheet">
  <section class="col-breakfast">
    <div class="brand"><span class="brand-dot"></span><span>The Thistle</span></div>
    <div class="side-rule"></div>
    <div class="side-title">BREAKFAST MENU <small>ALL DAY</small></div>

    <div class="item"><div class="item-row"><span class="item-name">toast - served buttered</span><span class="leader"></span><span class="item-price">$4.5</span></div></div>
    <div class="item"><div class="item-row"><span class="item-name">toast</span><span class="item-desc">- sourdough white or wholemeal</span><span class="leader"></span><span class="item-price">+$0.5</span></div></div>
    <div class="item"><div class="item-row"><span class="item-name">gf bread (2)</span><span class="leader"></span><span class="item-price">$5.5</span></div></div>
    <div class="item"><div class="item-row"><span class="item-name">turkish raisin (2) toast</span><span class="leader"></span><span class="item-price">$5.5</span></div></div>
    <div class="item"><div class="item-row"><span class="item-name">banana bread (gf)</span><span class="leader"></span><span class="item-price">$5.5</span></div></div>
    <div class="item"><div class="item-row"><span class="item-name">granola muesli</span><span class="item-desc">home made with</span><span class="leader"></span><span class="item-price">$12.5</span></div><div class="item-desc">yoghurt &amp; our own berry compote</div></div>
    <div class="item"><div class="item-row"><span class="item-name">spanish eggs</span><span class="item-desc">two poached range eggs</span><span class="leader"></span><span class="item-price">$12.5</span></div><div class="item-desc">in a warm spanish tomato salsa topped w/ parmesan cheese with toasted sourdough &nbsp; w/ chorizo $14.5</div></div>
    <div class="item"><div class="item-row"><span class="item-name">bacon &amp; eggs</span><span class="item-desc">(poached / scrambled or fried)</span><span class="leader"></span><span class="item-price">$13.5</span></div><div class="item-desc">on s/dough toast &amp; side of relish</div></div>
    <div class="item"><div class="item-row"><span class="item-name">bacon &amp; eggs sandwich</span><span class="leader"></span><span class="item-price">$9.0</span></div><div class="item-desc">turkish bread lightly toasted with (2) bacon, fried egg &amp; your choice of <b>house relish / hollandaise / tom or bbq sauce</b></div></div>
    <div class="item"><div class="item-row"><span class="item-name">eggs benedict</span><span class="item-desc">toasted sourdough w baby</span><span class="leader"></span><span class="item-price">$16.5</span></div><div class="item-desc">spinach, poached eggs &amp; hollandaise sauce &nbsp;<b>$12.5 / w mush $16.5 / w leg ham $16.5 / w bacon $16.5 / w salmon $18.5</b></div></div>
    <div class="item"><div class="item-row"><span class="item-name">the big thistle breakfast</span><span class="leader"></span><span class="item-price">$19.5</span></div><div class="item-desc">toasted sourdough, bacon, eggs (poached, scrambled or fried), chorizo, tomato, mushrooms, baby spinach, hash brown w/ house relish</div></div>
    <div class="item"><div class="item-row"><span class="item-name">french toast</span><span class="item-desc">brioche bread soaked in a creamy</span><span class="leader"></span><span class="item-price">$15.5</span></div><div class="item-desc">cinnamon mix, fried &amp; served with maple syrup, vanilla ice-cream &amp; a side of our berry compote</div></div>
    <div class="item"><div class="item-row"><span class="item-name">pancakes</span><span class="item-desc">two stack of pancakes, topped</span><span class="leader"></span><span class="item-price">$12.5</span></div><div class="item-desc">w maple syrup &amp; ice cream &nbsp; add grilled banana +$2.0</div></div>
    <div class="item"><div class="item-row"><span class="item-name">breakfast wrap</span><span class="item-desc">bacon, fried egg, spinach,</span><span class="leader"></span><span class="item-price">$13.5</span></div><div class="item-desc">cheese topped with house made relish</div></div>
    <div class="item"><div class="item-row"><span class="item-name">croissants</span><span class="item-desc">ham, cheese &amp; tomato</span><span class="leader"></span><span class="item-price">$8.5</span></div><div class="item-desc">or ham, cheese &amp; avocado &nbsp; $9.5</div></div>

    <div class="extras">
      <span class="extras-label">Extras / Sides</span>
      <div class="extras-row"><span class="price">$4 ea</span><span class="list">bacon (2) - egg (2) - chorizo - salmon - mushrooms</span></div>
      <div class="extras-row"><span class="price">$2 ea</span><span class="list">grilled tomato - baby spinach (wilted) - avocado - hash brown</span></div>
    </div>
  </section>

  <section class="col-lunch">
    <div class="lunch-band">
      <h1>Lunch<br>Menu</h1>
      <div class="hours">MON TO FRI 7.30am /<br>SAT &amp; SUN<br>from 11.30am</div>
    </div>

    <div class="section-head"><span>Wraps</span></div>
    <div class="section-note">lightly toasted &amp; served w/ beer battered chips</div>
    <div class="item"><div class="item-row"><span class="item-name">chicken</span><span class="item-desc">w/ bacon, mixed lettuce, tasty cheese</span><span class="leader"></span><span class="item-price">$15.0</span></div><div class="item-desc">&amp; your choice of sauce <b>(sweet chilli &amp; sour cream / caesar / aioli / ranch dressing)</b></div></div>
    <div class="item"><div class="item-row"><span class="item-name">thistle</span><span class="item-desc">mixed lettuce, sundried tomato, bacon</span><span class="leader"></span><span class="item-price">$16.5</span></div><div class="item-desc">crumbed chicken, tasty cheese &amp; aioli</div></div>
    <div class="item"><div class="item-row"><span class="item-name">vegie wrap</span><span class="item-desc">grilled mushrooms, capsicum, onion</span><span class="leader"></span><span class="item-price">$15.5</span></div><div class="item-desc">tomato, fetta, spinach and a balsamic glaze</div></div>
    <div class="item"><div class="item-row"><span class="item-name">lentil wrap</span><span class="item-desc">our own lentil patty w/ lettuce, tomato</span><span class="leader"></span><span class="item-price">$15.5</span></div><div class="item-desc">avocado, cheese, mango chutney &amp; sour cream</div></div>
    <div class="item"><div class="item-row"><span class="item-name">chicken fajita</span><span class="item-desc">seasoned chicken w/ capsicum</span><span class="leader"></span><span class="item-price">$16.5</span></div><div class="item-desc">onion, our guacamole, cheese &amp; salsa served w a side of sour cream</div></div>
    <div class="item"><div class="item-row"><span class="item-name">beef burrito</span><span class="item-desc">seasoned pulled beef, brown rice</span><span class="leader"></span><span class="item-price">$16.5</span></div><div class="item-desc">beans, lettuce, cheese, guacamole, spicy salsa &amp; sour cream</div></div>

    <div class="section-head"><span>Burgers</span></div>
    <div class="section-note">made on fresh toasted turkish bread &amp; served w/ beer battered chips</div>
    <div class="item"><div class="item-row"><span class="item-name">b.l.a.t</span><span class="item-desc">bacon, mixed lettuce, avocado &amp;</span><span class="leader"></span><span class="item-price">$14.5</span></div><div class="item-desc">fresh tomato, aioli</div></div>
    <div class="item"><div class="item-row"><span class="item-name">lentil burger</span><span class="item-desc">our own lentil patty, cheese, tomato</span><span class="leader"></span><span class="item-price">$15.5</span></div><div class="item-desc">avocado, lettuce, mango chutney &amp; sour cream</div></div>
    <div class="item"><div class="item-row"><span class="item-name">schnitzel burger</span><span class="item-desc">house made schnitzel, bacon</span><span class="leader"></span><span class="item-price">$18.0</span></div><div class="item-desc">lettuce, tasty cheese w/ your choice of sweet chilli &amp; sour cream / caesar dressing / aioli / ranch</div></div>
    <div class="item"><div class="item-row"><span class="item-name">american burger</span><span class="item-desc">150g house made patty w/ cheese</span><span class="leader"></span><span class="item-price">$16.5</span></div><div class="item-desc">tomato, lettuce, pickles, tomato ketchup, mustard &amp; mayo</div></div>
    <div class="item"><div class="item-row"><span class="item-name">grilled chicken burger</span><span class="leader"></span><span class="item-price">$16.5</span></div><div class="item-desc">char grilled chicken breast, cheese, avocado, tomato, lettuce &amp; your choice of sauce <b>(sweet chilli &amp; sour cream / caesar / aioli / ranch dressing)</b></div></div>

    <div class="section-head"><span>House Made Chicken Schnitzels</span></div>
    <div class="section-note">all schnitzels are prepared freshly in house &amp; served w/ a side salad &amp; beer battered chips</div>
    <div class="item"><div class="item-row"><span class="item-name">housemade schnitzel</span><span class="item-desc">w/ your choice of</span><span class="leader"></span><span class="item-price">$19.5</span></div><div class="item-desc">mushroom, pepper or plain gravy</div></div>
    <div class="item"><div class="item-row"><span class="item-name">chicken &amp; avocado</span><span class="leader"></span><span class="item-price">$23.5</span></div><div class="item-desc">schnitzel topped w/ fresh avocado &amp; cheese grilled</div></div>
    <div class="item"><div class="item-row"><span class="item-name">parma</span><span class="item-desc">schnitzel topped w/ our tomato sauce</span><span class="leader"></span><span class="item-price">$23.5</span></div><div class="item-desc">ham &amp; grilled w/ cheese</div></div>
    <div class="item"><div class="item-row"><span class="item-name">hawaiian</span><span class="item-desc">schnitzel topped w/ leg ham</span><span class="leader"></span><span class="item-price">$23.5</span></div><div class="item-desc">pineapple &amp; tasty cheese</div></div>
  </section>

  <footer class="footer">
    <strong>Most items can be made gluten free * (+$1.0)</strong><br>
    chorizo (gf) &nbsp; bacon (gf) &nbsp; ham (gf) &nbsp; relish (gf) &nbsp; hash browns (gf)<br>
    <strong>Vegans - we are more than happy to make something to suit you</strong>
  </footer>
</main>
</body>
</html>
```